Flyer Design for Earthworks Business in Australia

Bluegum Ridge Earthworks is a new Earthworks and mini excavator business in Australia that requires an attention grabbing flyer to be used in our promotional material.

It will be dual sided and will be used for print media and also digital marketing. It will incorporate our logo, contact details and a list of our services offered.

Target Market(s)

Prospective clients that require earthworks

Industry/Entity Type

Construction and Earthworks

Requirements
Must have
• Must be dual sided, include our logo and contact information (phone number and Web page) and our services offered.
Nice to have
• QR link for Web site. Some photo(s) incorporated into the design.

```html
<!DOCTYPE html>
<html lang="en">
<head>
<meta charset="utf-8">
<title>Bluegum Ridge Earthworks – Flyer</title>
<link href="https://fonts.googleapis.com/css2?family=Barlow+Condensed:ital,wght@1,700;1,800&family=Roboto:wght@400;500;700&display=swap" rel="stylesheet">
<style>
  :root{
    --lime:#c5d92d;
    --black:#0b0b0b;
    --white:#ffffff;
    --grey-bg:#6e7174;
    --text-grey:#555555;
  }
  html,body{margin:0;padding:0;width:1200px;height:1200px;overflow:hidden;background:var(--grey-bg);}
  .stage{position:absolute;left:0;top:0;width:1932px;height:1932px;transform:scale(0.62112);transform-origin:0 0;}
  .page{position:absolute;top:399px;width:803px;height:1134px;background:var(--white);overflow:hidden;font-family:"Roboto",sans-serif;}
  .page--front{left:122px;}
  .page--back{left:1000px;}
  .page svg.shapes{position:absolute;left:0;top:0;width:803px;height:1134px;}
  .abs{position:absolute;margin:0;}
  .brand{display:flex;align-items:center;gap:12px;}
  .brand__mark{width:26px;height:26px;background:var(--lime);flex:none;}
  .brand__name{font-family:"Roboto",sans-serif;font-weight:700;font-size:25px;line-height:1.05;color:var(--black);letter-spacing:1px;text-transform:uppercase;}
  .display{font-family:"Barlow Condensed",sans-serif;font-style:italic;font-weight:800;text-transform:uppercase;line-height:1;}
  .headline{left:52px;top:256px;font-size:52px;line-height:0.92;color:var(--black);letter-spacing:0.5px;}
  .tab-title{font-size:40px;color:var(--white);}
  .about{left:52px;top:563px;width:360px;font-size:15.5px;line-height:1.27;color:var(--text-grey);}
  .about p{margin:0 0 11px;}
  .slogan{left:52px;top:806px;font-size:38px;color:var(--black);}
  .commit-intro{left:64px;top:870px;font-size:15px;color:var(--black);}
  .pledges{left:52px;top:920px;width:720px;display:grid;grid-template-columns:388px 1fr;row-gap:9px;list-style:none;padding:0;font-size:16px;color:var(--white);}
  .pledges li{display:flex;align-items:center;gap:7px;}
  .tick{width:14px;height:14px;flex:none;}
  .closing{left:52px;top:987px;width:720px;font-size:16px;line-height:1.25;color:var(--white);}
  .phone-number{top:1063px;font-size:52px;color:var(--black);}
  .contact{list-style:none;padding:0;font-size:14.5px;line-height:20px;}
  .contact li{display:flex;align-items:center;gap:9px;}
  .contact svg{width:13px;height:13px;flex:none;}
  .contact--dark{left:548px;top:1058px;color:var(--black);}
  .contact--light{left:548px;top:1058px;color:var(--white);}
  .service{position:absolute;margin:0;}
  .service__title{font-family:"Barlow Condensed",sans-serif;font-style:italic;font-weight:800;font-size:26px;text-transform:uppercase;margin:0 0 8px;line-height:1;}
  .service__text{font-size:13.3px;line-height:1.22;margin:0;}
  .service--dark{left:248px;width:480px;}
  .service--dark .service__title{color:var(--lime);}
  .service--dark .service__text{color:var(--white);}
  .service--light{left:80px;width:500px;}
  .service--light .service__title{color:var(--black);}
  .service--light .service__text{color:var(--black);}
</style>
</head>
<body>
<div class="stage">

  <!-- FRONT PAGE -->
  <section class="page page--front">
    <svg class="shapes" viewBox="0 0 803 1134" aria-hidden="false">
      <defs>
        <linearGradient id="trenchPhoto" x1="0" y1="0" x2="1" y2="1">
          <stop offset="0" stop-color="#e8cf1e"/>
          <stop offset="0.45" stop-color="#7f9a52"/>
          <stop offset="1" stop-color="#6b4a2c"/>
        </linearGradient>
        <linearGradient id="loaderPhoto" x1="0" y1="0" x2="1" y2="1">
          <stop offset="0" stop-color="#f0f0ea"/>
          <stop offset="0.5" stop-color="#c9a23a"/>
          <stop offset="1" stop-color="#3a3328"/>
        </linearGradient>
      </defs>
      <!-- top stripes -->
      <polygon points="0,148 65,212 48,212 0,165" fill="var(--black)"/>
      <polygon points="0,172 40,212 22,212 0,190" fill="var(--black)"/>
      <line x1="390" y1="130" x2="310" y2="205" stroke="var(--black)" stroke-width="3"/>
      <line x1="400" y1="140" x2="325" y2="210" stroke="var(--black)" stroke-width="3"/>
      <line x1="410" y1="150" x2="340" y2="212" stroke="var(--black)" stroke-width="3"/>
      <!-- headline block -->
      <polygon points="0,215 352,215 575,440 560,470 50,470 0,420" fill="var(--lime)"/>
      <!-- photo -->
      <g role="img" aria-label="Photo of a yellow mini excavator arm digging a trench across a grassy field">
        <polygon points="300,0 803,0 803,437 575,437 355,212 420,145" fill="url(#trenchPhoto)"/>
      </g>
      <polyline points="296,0 420,145 355,212 575,440 803,440" fill="none" stroke="var(--black)" stroke-width="10"/>
      <line x1="610" y1="470" x2="660" y2="420" stroke="var(--black)" stroke-width="3"/>
      <line x1="625" y1="470" x2="675" y2="420" stroke="var(--black)" stroke-width="3"/>
      <line x1="640" y1="470" x2="690" y2="420" stroke="var(--black)" stroke-width="3"/>
      <!-- about tab -->
      <polygon points="0,422 52,474 400,474 390,486 308,486 252,542 45,542 0,498" fill="var(--black)"/>
      <!-- loader area -->
      <polygon points="570,458 803,458 803,730" fill="var(--lime)"/>
      <line x1="535" y1="485" x2="803" y2="770" stroke="var(--lime)" stroke-width="4"/>
      <line x1="550" y1="480" x2="803" y2="750" stroke="var(--lime)" stroke-width="4"/>
      <g role="img" aria-label="Cut-out photo of a yellow wheel loader with a raised bucket">
        <polygon points="420,500 780,500 780,780 420,780" fill="url(#loaderPhoto)" opacity="0.9"/>
      </g>
      <!-- slogan & commitments -->
      <polygon points="0,775 35,800 0,830" fill="var(--lime)"/>
      <polygon points="0,842 38,797 700,797 745,845 803,845 803,1050 0,1050" fill="var(--black)"/>
      <polygon points="50,800 655,800 688,850 30,850" fill="var(--lime)"/>
      <line x1="660" y1="800" x2="695" y2="848" stroke="var(--lime)" stroke-width="4"/>
      <line x1="672" y1="800" x2="707" y2="848" stroke="var(--lime)" stroke-width="4"/>
      <line x1="684" y1="800" x2="719" y2="848" stroke="var(--lime)" stroke-width="4"/>
      <line x1="690" y1="795" x2="740" y2="840" stroke="var(--black)" stroke-width="3"/>
      <line x1="740" y1="840" x2="803" y2="840" stroke="var(--black)" stroke-width="3"/>
      <polygon points="35,868 420,868 445,893 58,893" fill="var(--white)"/>
      <!-- footer -->
      <polygon points="0,1052 500,1052 582,1134 0,1134" fill="var(--lime)"/>
      <line x1="432" y1="1052" x2="514" y2="1134" stroke="var(--black)" stroke-width="4"/>
      <line x1="448" y1="1052" x2="530" y2="1134" stroke="var(--black)" stroke-width="4"/>
      <line x1="515" y1="1052" x2="597" y2="1134" stroke="var(--black)" stroke-width="3"/>
      <polygon points="25,1066 93,1066 110,1094 93,1124 25,1124 10,1094" fill="var(--black)"/>
      <path d="M48,1080 c-4,0 -7,4 -5,10 c3,10 12,19 22,22 c6,2 10,-1 10,-5 l-1,-4 l-8,-4 l-4,4 c-5,-2 -9,-6 -11,-11 l4,-4 l-4,-8 z" fill="var(--white)"/>
    </svg>

    <div class="abs brand" style="left:55px;top:92px;">
      <span class="brand__mark"></span>
      <span class="brand__name">Bluegum Ridge<br>Earthworks</span>
    </div>

    <h1 class="abs display headline">Precision<br>Earthworks.<br>Solid Foundations.<br>Built to Last.</h1>

    <h2 class="abs display tab-title" style="left:55px;top:497px;">About Us</h2>
    <div class="abs about">
      <p>Bluegum Ridge Earthworks is your Perth based mini excavator and earthworks business delivering precise, efficient, and dependable excavation services for residential and small commercial projects.</p>
      <p>We understand that every successful build begins with solid groundwork. That’s why we focus on accuracy, site safety, and attention to detail on every job — no matter the size.</p>
    </div>

    <h2 class="abs display slogan">Precision. Integrity. Performance.</h2>
    <p class="abs commit-intro">At Bluegum Ridge Earthworks, we are committed to:</p>
    <ul class="abs pledges">
      <li><svg class="tick" viewBox="0 0 14 14"><circle cx="7" cy="7" r="7" fill="var(--lime)"/><path d="M4 7.2l2 2 4-4.4" stroke="var(--black)" stroke-width="1.8" fill="none"/></svg>Delivering high-quality workmanship</li>
      <li><svg class="tick" viewBox="0 0 14 14"><circle cx="7" cy="7" r="7" fill="var(--lime)"/><path d="M4 7.2l2 2 4-4.4" stroke="var(--black)" stroke-width="1.8" fill="none"/></svg>Completing projects safely and efficiently</li>
      <li><svg class="tick" viewBox="0 0 14 14"><circle cx="7" cy="7" r="7" fill="var(--lime)"/><path d="M4 7.2l2 2 4-4.4" stroke="var(--black)" stroke-width="1.8" fill="none"/></svg>Maintaining clear and honest communication</li>
      <li><svg class="tick" viewBox="0 0 14 14"><circle cx="7" cy="7" r="7" fill="var(--lime)"/><path d="M4 7.2l2 2 4-4.4" stroke="var(--black)" stroke-width="1.8" fill="none"/></svg>Providing reliable service you can count on</li>
    </ul>
    <p class="abs closing">We approach every project with professionalism and pride, ensuring your site is prepared correctly and ready for the next stage of development.</p>

    <p class="abs display phone-number" style="left:115px;">0412 555 318</p>
    <ul class="abs contact contact--dark">
      <li><svg viewBox="0 0 13 13"><circle cx="6.5" cy="6.5" r="6.5" fill="var(--lime)"/><circle cx="6.5" cy="5.5" r="2" fill="var(--black)"/></svg>Redgum Vale, Western Australia</li>
      <li><svg viewBox="0 0 13 13"><circle cx="6.5" cy="6.5" r="6.5" fill="var(--lime)"/><rect x="3" y="4" width="7" height="5" fill="var(--black)"/></svg>admin@bluegumridge.com.au</li>
      <li><svg viewBox="0 0 13 13"><circle cx="6.5" cy="6.5" r="6.5" fill="var(--lime)"/><circle cx="6.5" cy="6.5" r="3.5" fill="none" stroke="var(--black)" stroke-width="1.3"/></svg>www.bluegumridge.com.au</li>
    </ul>
  </section>

  <!-- BACK PAGE -->
  <section class="page page--back">
    <svg class="shapes" viewBox="0 0 803 1134">
      <defs>
        <linearGradient id="miniPhoto" x1="0" y1="0" x2="1" y2="1">
          <stop offset="0" stop-color="#7fa05a"/>
          <stop offset="0.5" stop-color="#e3c62a"/>
          <stop offset="1" stop-color="#9a9a92"/>
        </linearGradient>
        <linearGradient id="soilPhoto" x1="0" y1="0" x2="1" y2="1">
          <stop offset="0" stop-color="#b9c4cc"/>
          <stop offset="1" stop-color="#8a6a48"/>
        </linearGradient>
      </defs>
      <polygon points="0,165 42,205 0,205" fill="var(--black)"/>
      <rect x="0" y="203" width="803" height="22" fill="var(--black)"/>
      <polygon points="803,150 803,205 755,205" fill="var(--black)"/>
      <polygon points="362,128 440,205 395,205 362,172" fill="var(--black)"/>
      <g role="img" aria-label="Photo of a yellow mini excavator with attachments parked on paving">
        <polygon points="378,0 803,0 803,145 758,192 440,192 368,122" fill="url(#miniPhoto)"/>
      </g>
      <polyline points="372,0 368,122 440,192 758,192" fill="none" stroke="var(--black)" stroke-width="5"/>
      <line x1="350" y1="125" x2="420" y2="200" stroke="var(--black)" stroke-width="3"/>
      <line x1="352" y1="140" x2="410" y2="203" stroke="var(--black)" stroke-width="3"/>
      <polygon points="210,222 585,222 548,260 248,260" fill="var(--black)"/>

      <!-- row 1 dark -->
      <polygon points="58,290 740,290 757,308 757,390 58,390" fill="var(--black)"/>
      <g role="img" aria-label="Photo of an excavator bucket digging into sandy soil">
        <polygon points="67,276 200,276 215,291 215,398 80,398 67,385" fill="url(#soilPhoto)" stroke="var(--black)" stroke-width="4"/>
      </g>
      <!-- row 2 light -->
      <polygon points="55,414 757,414 757,512 75,512 55,494" fill="var(--lime)"/>
      <g role="img" aria-label="Photo of a yellow excavator arm cutting a trench in grass">
        <polygon points="598,405 735,405 748,418 748,527 612,527 598,513" fill="url(#trenchPhotoB)" stroke="var(--black)" stroke-width="4"/>
      </g>
      <!-- row 3 dark -->
      <polygon points="58,540 740,540 757,558 757,638 58,638" fill="var(--black)"/>
      <g role="img" aria-label="Photo of excavators beside a water-filled drainage channel in red earth">
        <polygon points="67,527 200,527 215,542 215,648 80,648 67,635" fill="url(#soilPhoto)" stroke="var(--black)" stroke-width="4"/>
      </g>
      <!-- row 4 light -->
      <polygon points="55,662 757,662 757,760 75,760 55,742" fill="var(--lime)"/>
      <g role="img" aria-label="Photo of a freshly levelled concrete slab being finished">
        <polygon points="598,653 735,653 748,666 748,775 612,775 598,761" fill="#a7aaa6" stroke="var(--black)" stroke-width="4"/>
      </g>
      <!-- row 5 dark -->
      <polygon points="58,790 740,790 757,808 757,888 58,888" fill="var(--black)"/>
      <g role="img" aria-label="Photo of reinforcing steel laid in footing trenches">
        <polygon points="67,775 200,775 215,790 215,897 80,897 67,884" fill="#8f8a80" stroke="var(--black)" stroke-width="4"/>
      </g>
      <!-- row 6 light -->
      <polygon points="55,912 757,912 757,1010 75,1010 55,992" fill="var(--lime)"/>
      <g role="img" aria-label="Photo of an operator seated in a machine cab">
        <polygon points="598,903 735,903 748,916 748,1025 612,1025 598,1011" fill="#c08a3a" stroke="var(--black)" stroke-width="4"/>
      </g>
      <defs>
        <linearGradient id="trenchPhotoB" x1="0" y1="0" x2="1" y2="1">
          <stop offset="0" stop-color="#e8cf1e"/>
          <stop offset="0.5" stop-color="#7f9a52"/>
          <stop offset="1" stop-color="#6b4a2c"/>
        </linearGradient>
      </defs>

      <!-- footer -->
      <polygon points="0,1052 430,1052 512,1134 0,1134" fill="var(--lime)"/>
      <polygon points="470,1052 803,1052 803,1134 552,1134" fill="var(--black)"/>
      <line x1="440" y1="1052" x2="522" y2="1134" stroke="var(--black)" stroke-width="4"/>
      <line x1="455" y1="1052" x2="537" y2="1134" stroke="var(--black)" stroke-width="4"/>
      <polygon points="25,1066 93,1066 110,1094 93,1124 25,1124 10,1094" fill="var(--black)"/>
      <path d="M48,1080 c-4,0 -7,4 -5,10 c3,10 12,19 22,22 c6,2 10,-1 10,-5 l-1,-4 l-8,-4 l-4,4 c-5,-2 -9,-6 -11,-11 l4,-4 l-4,-8 z" fill="var(--lime)"/>
    </svg>

    <div class="abs brand" style="left:48px;top:88px;">
      <span class="brand__mark"></span>
      <span class="brand__name">Bluegum Ridge<br>Earthworks</span>
    </div>

    <h2 class="abs display tab-title" style="left:272px;top:220px;">Our Services</h2>

    <article class="service service--dark" style="top:305px;">
      <h3 class="service__title">Excavation &amp; Site Preparation</h3>
      <p class="service__text">Here at Bluegum Ridge, we can provide comprehensive excavation and site preparation services to ensure your project starts on solid ground.</p>
    </article>
    <article class="service service--light" style="top:425px;">
      <h3 class="service__title">Trenching</h3>
      <p class="service__text">Our trenching services are designed to support utility installations, drainage systems, and foundation requirements. We use advanced equipment to create clean, accurate trenches while maintaining site safety and minimising disruption.</p>
    </article>
    <article class="service service--dark" style="top:551px;">
      <h3 class="service__title">Drainage &amp; Earthmoving Support</h3>
      <p class="service__text">Proper drainage is essential for the longevity and safety of any structure. We provide reliable drainage solutions and earthmoving support to manage water flow and protect your property from erosion or flooding issues.</p>
    </article>
    <article class="service service--light" style="top:673px;">
      <h3 class="service__title">Pad and Slab Preparation</h3>
      <p class="service__text">A properly prepared pad or slab base is critical for structural integrity. We carefully level, compact, and prepare the ground to meet engineering specifications, ensuring durability and long-term performance.</p>
    </article>
    <article class="service service--dark" style="top:801px;">
      <h3 class="service__title">Footings &amp; Foundations</h3>
      <p class="service__text">Strong foundations begin with expert groundwork. We excavate and prepare footings according to structural plans, ensuring stability and compliance with construction standards.</p>
    </article>
    <article class="service service--light" style="top:930px;">
      <h3 class="service__title">Machine Hire with Operator</h3>
      <p class="service__text">Need reliable equipment with experienced operators? We offer machine hire services with fully qualified operators to support your project efficiently and safely.</p>
    </article>

    <p class="abs display phone-number" style="left:115px;">0412 555 318</p>
    <ul class="abs contact contact--light">
      <li><svg viewBox="0 0 13 13"><circle cx="6.5" cy="6.5" r="6.5" fill="var(--lime)"/><circle cx="6.5" cy="5.5" r="2" fill="var(--black)"/></svg>Redgum Vale, Western Australia</li>
      <li><svg viewBox="0 0 13 13"><circle cx="6.5" cy="6.5" r="6.5" fill="var(--lime)"/><rect x="3" y="4" width="7" height="5" fill="var(--black)"/></svg>admin@bluegumridge.com.au</li>
      <li><svg viewBox="0 0 13 13"><circle cx="6.5" cy="6.5" r="6.5" fill="var(--lime)"/><circle cx="6.5" cy="6.5" r="3.5" fill="none" stroke="var(--black)" stroke-width="1.3"/></svg>www.bluegumridge.com.au</li>
    </ul>
  </section>

</div>
</body>
</html>
```